Valdrenix is a medical device company that needs a new look for their Packaging Design

Valdrenix is a medical device company that needs a new look for their packaging design. It should look clean and sophisticated. The logo must not be changed. Please maintain the branding of the logo.

You may refer to the attachments for our logo and the packaging template we want designed.

Industry/Entity Type

It Company

```html
<!DOCTYPE html>
<html lang="en">
<head>
<meta charset="utf-8">
<title>Valdrenix – Aspheric Intraocular Lens Carton Dieline</title>
<link rel="stylesheet" href="https://fonts.googleapis.com/css2?family=Roboto:wght@300;400;700&family=Roboto+Condensed:wght@700&display=swap">
<style>
  :root {
    --stage: #e8e9eb;
    --carton-blue: #1c6db3;
    --front-blue: #0b6cbf;
    --fold-line: #5d9bd3;
    --ink-white: #ffffff;
  }
  html, body {
    margin: 0;
    padding: 0;
    width: 1200px;
    height: 1000px;
    overflow: hidden;
    background: var(--stage);
  }
  .dieline {
    display: block;
    width: 1200px;
    height: 1000px;
  }
  .panel { fill: var(--carton-blue); }
  .panel-front { fill: var(--front-blue); }
  .fold { stroke: var(--fold-line); stroke-width: 0.8; fill: none; }
  .accent-disc { fill: var(--ink-white); }
  .brand-name {
    font-family: "Roboto", Arial, sans-serif;
    font-weight: 300;
    fill: var(--ink-white);
    letter-spacing: 1px;
  }
  .product-line {
    font-family: "Roboto", Arial, sans-serif;
    font-weight: 700;
    fill: var(--ink-white);
    font-size: 9px;
  }
  .lens-type {
    font-family: "Roboto Condensed", "Arial Narrow", sans-serif;
    font-weight: 700;
    fill: var(--ink-white);
  }
  .lens-sub {
    font-family: "Roboto", Arial, sans-serif;
    font-weight: 700;
    fill: var(--ink-white);
    font-size: 9px;
  }
  .fine-print {
    font-family: "Roboto", Arial, sans-serif;
    font-weight: 400;
    fill: var(--ink-white);
    font-size: 5.6px;
  }
  .icon-line { fill: none; stroke: var(--ink-white); stroke-width: 1.1; }
  .icon-label {
    font-family: "Roboto", Arial, sans-serif;
    font-weight: 700;
    fill: var(--ink-white);
    font-size: 4.5px;
  }
</style>
</head>
<body>
<svg class="dieline" viewBox="0 0 1200 1000" xmlns="http://www.w3.org/2000/svg" role="img" aria-label="Flat carton dieline for the Valdrenix aspheric intraocular lens">
  <defs>
    <clipPath id="clip-front"><rect x="597" y="205" width="361" height="253"/></clipPath>
    <clipPath id="clip-back"><rect x="597" y="557" width="361" height="258"/></clipPath>

    <g id="warning-icons">
      <rect x="0" y="0" width="26" height="10" class="icon-line"/>
      <text x="13" y="6.8" text-anchor="middle" class="icon-label">STERILE EO</text>
      <path d="M38 10 L44 0 L50 10 Z" class="icon-line"/>
      <circle cx="63" cy="5" r="5" class="icon-line"/>
      <line x1="59.5" y1="8.5" x2="66.5" y2="1.5" class="icon-line"/>
      <circle cx="80" cy="5" r="5" class="icon-line"/>
      <line x1="76.5" y1="8.5" x2="83.5" y2="1.5" class="icon-line"/>
      <circle cx="97" cy="5" r="5" class="icon-line"/>
      <line x1="93.5" y1="8.5" x2="100.5" y2="1.5" class="icon-line"/>
    </g>
  </defs>

  <!-- top tuck flap and dust flaps -->
  <g class="top-closure">
    <path class="panel" d="M597 205 L597 103 L958 103 L958 205 Z"/>
    <path class="panel" d="M511 205 L511 125 L520 118 L590 118 L597 125 L597 205 Z"/>
    <path class="panel" d="M958 205 L958 125 L965 118 L1035 118 L1044 125 L1044 205 Z"/>
    <g transform="rotate(180 735 150)" class="company-address">
      <text x="735" y="140" text-anchor="middle" class="fine-print">Meridian Ocular Systems Ltd</text>
      <text x="735" y="148" text-anchor="middle" class="fine-print">Harrow House, Lindell Avenue, Ashbridge, AB4 2RT, UK</text>
      <text x="735" y="156" text-anchor="middle" class="fine-print">Website: www.meridian-ocular.com    E-mail: info@meridian-ocular.com</text>
      <text x="735" y="176" text-anchor="middle" class="fine-print">REV.06 MOS0062015</text>
    </g>
  </g>

  <!-- side panels -->
  <g class="side-panel side-left">
    <path class="panel" d="M597 205 L597 458 L458 458 Q447 458 447 447 L447 216 Q447 205 458 205 Z"/>
    <line x1="497" y1="205" x2="497" y2="458" class="fold"/>
    <g transform="translate(545 215) rotate(90)">
      <text x="0" y="0" class="brand-name" font-size="34">Valdrenix</text>
    </g>
    <g transform="translate(526 215) rotate(90)">
      <text x="0" y="0" class="lens-type" font-size="15">ASPHERIC</text>
      <text x="0" y="8" class="lens-sub" font-size="5.5">WITH 360° SQUARE EDGE</text>
    </g>
    <g transform="translate(524 328) rotate(90)">
      <use href="#warning-icons"/>
    </g>
  </g>

  <g class="side-panel side-right">
    <path class="panel" d="M958 205 L1097 205 Q1108 205 1108 216 L1108 447 Q1108 458 1097 458 L958 458 Z"/>
    <line x1="1058" y1="205" x2="1058" y2="458" class="fold"/>
    <g transform="translate(1010 440) rotate(-90)">
      <text x="0" y="0" class="brand-name" font-size="34">Valdrenix</text>
    </g>
    <g transform="translate(1033 440) rotate(-90)">
      <text x="0" y="0" class="lens-type" font-size="15">ASPHERIC</text>
      <text x="0" y="8" class="lens-sub" font-size="5.5">WITH 360° SQUARE EDGE</text>
    </g>
    <g transform="translate(1031 318) rotate(-90)">
      <use href="#warning-icons"/>
    </g>
  </g>

  <!-- front panel -->
  <g class="front-panel">
    <rect x="597" y="205" width="361" height="253" class="panel-front"/>
    <g clip-path="url(#clip-front)">
      <circle cx="640" cy="400" r="125" class="accent-disc"/>
    </g>
    <text x="780" y="262" text-anchor="middle" class="brand-name" font-size="44">Valdrenix</text>
    <text x="765" y="279" class="product-line">HYDROPHOBIC ACRYLIC</text>
    <text x="765" y="290" class="product-line">INTRAOCULAR LENS</text>
    <text x="793" y="418" class="lens-type" font-size="25">ASPHERIC</text>
    <text x="793" y="431" class="lens-sub">WITH 360° SQUARE EDGE</text>
  </g>

  <!-- bottom band with dust flaps -->
  <g class="bottom-band">
    <path class="panel" d="M597 458 L958 458 L958 557 L597 557 Z"/>
    <path class="panel" d="M511 458 L597 458 L597 535 L590 542 L520 542 L511 535 Z"/>
    <path class="panel" d="M958 458 L1044 458 L1044 535 L1035 542 L965 542 L958 535 Z"/>
    <text x="615" y="505" class="brand-name" font-size="40">Valdrenix</text>
    <text x="615" y="527" class="product-line">HYDROPHOBIC ACRYLIC INTRAOCULAR LENS</text>
    <text x="615" y="539" class="product-line">ASPHERIC WITH 360° SQUARE EDGE</text>
  </g>

  <!-- back panel -->
  <g class="back-panel">
    <rect x="597" y="557" width="361" height="258" class="panel"/>
    <line x1="597" y1="557" x2="958" y2="557" class="fold"/>
    <g clip-path="url(#clip-back)">
      <circle cx="640" cy="752" r="120" class="accent-disc"/>
    </g>
    <text x="614" y="595" class="lens-type" font-size="25">ASPHERIC</text>
    <text x="614" y="608" class="lens-sub">WITH 360° SQUARE EDGE</text>

    <g class="multilingual-notice">
      <text x="795" y="580" class="fine-print">Contains one sterile intraocular lens</text>
      <text x="795" y="587" class="fine-print">Do not use if the packaging is damaged</text>
      <text x="795" y="594" class="fine-print">Do not resterilize</text>

      <text x="795" y="603" class="fine-print">Bevat één steriele intraoculaire lens</text>
      <text x="795" y="610" class="fine-print">Niet gebruiken als de verpakking beschadigd is</text>
      <text x="795" y="617" class="fine-print">Niet opnieuw steriliseren</text>

      <text x="795" y="626" class="fine-print">Contient une lentille intraoculaire stérile</text>
      <text x="795" y="633" class="fine-print">Ne pas utiliser si l'emballage est endommagé</text>
      <text x="795" y="640" class="fine-print">Ne pas restériliser</text>

      <text x="795" y="649" class="fine-print">Enthält eine sterile Intraokularlinse</text>
      <text x="795" y="656" class="fine-print">Nicht verwenden, wenn die Verpackung beschädigt ist</text>
      <text x="795" y="663" class="fine-print">Nicht resterilisieren</text>

      <text x="795" y="672" class="fine-print">Περιέχει έναν αποστειρωμένο ενδοφθάλμιο φακό</text>
      <text x="795" y="679" class="fine-print">Μην χρησιμοποιείτε αν η συσκευασία έχει φθαρεί</text>
      <text x="795" y="686" class="fine-print">Μην επαναποστειρώνετε</text>

      <text x="795" y="695" class="fine-print">Contiene una lente intraoculare sterile</text>
      <text x="795" y="702" class="fine-print">Non usare se la confezione è danneggiata</text>
      <text x="795" y="709" class="fine-print">Non risterilizzare</text>

      <text x="795" y="718" class="fine-print">Contém uma lente intra-ocular esterilizada</text>
      <text x="795" y="725" class="fine-print">Não use se a embalagem está danificada</text>
      <text x="795" y="732" class="fine-print">Não reesterilize</text>

      <text x="795" y="741" class="fine-print">Contiene una lente intraocular estéril</text>
      <text x="795" y="748" class="fine-print">No utilizar si el envase está dañado</text>
      <text x="795" y="755" class="fine-print">No vuelva a esterilizar</text>
    </g>

    <g transform="translate(797 773)">
      <use href="#warning-icons"/>
    </g>
  </g>

  <!-- bottom tuck -->
  <path class="panel" d="M597 815 L958 815 L955 838 Q954 845 947 845 L608 845 Q601 845 600 838 Z"/>
  <line x1="597" y1="815" x2="958" y2="815" class="fold"/>

  <!-- fold lines -->
  <g class="fold-lines">
    <line x1="597" y1="205" x2="958" y2="205" class="fold"/>
    <line x1="597" y1="458" x2="958" y2="458" class="fold"/>
    <line x1="597" y1="118" x2="597" y2="205" class="fold"/>
    <line x1="958" y1="118" x2="958" y2="205" class="fold"/>
    <line x1="597" y1="458" x2="597" y2="542" class="fold"/>
    <line x1="958" y1="458" x2="958" y2="542" class="fold"/>
  </g>
</svg>
</body>
</html>
```